Professional Simple Business Card Design

Design a professional business card . Simple Design.
Base colour White and purple(logo colour) which is from the logo attached. Other logo colour(orange) can be used if required.
Include dummy name and designation column which can be filled for later purpose.

Find attached Logo and other details.

```html
<!DOCTYPE html>
<html lang="en">
<head>
<meta charset="utf-8">
<title>Velora Formulations – Business Card</title>
<link rel="stylesheet" href="https://fonts.googleapis.com/css2?family=Montserrat:wght@400;500;600&display=swap">
<style>
  :root {
    --backdrop: #1b1b1d;
    --card: #f4f4f6;
    --purple: #8a4fb3;
    --orange: #f0a02c;
    --ink: #6b4a86;
    --rule: #d9cfe3;
  }
  * { margin: 0; padding: 0; box-sizing: border-box; }
  html, body { width: 1200px; height: 685px; overflow: hidden; }
  body {
    background: var(--backdrop);
    font-family: "Montserrat", Arial, sans-serif;
    display: flex;
    align-items: center;
    justify-content: center;
    gap: 60px;
  }
  .card {
    width: 520px;
    height: 297px;
    background: var(--card);
    border-radius: 3px;
    box-shadow: 0 10px 30px rgba(0,0,0,.45);
    position: relative;
    display: flex;
    align-items: center;
  }
  .brand {
    display: flex;
    align-items: center;
    gap: 14px;
  }
  .brand-dot {
    width: 26px; height: 26px;
    border-radius: 50%;
    background: var(--orange);
    flex: none;
  }
  .brand-name {
    color: var(--purple);
    font-weight: 600;
    font-size: 30px;
    line-height: 1.05;
    letter-spacing: .5px;
    text-transform: uppercase;
  }
  .card-front { justify-content: center; }

  .card-back { padding: 0 28px; gap: 26px; }
  .identity {
    width: 200px;
    flex: none;
    display: flex;
    flex-direction: column;
    gap: 22px;
  }
  .card-back .brand { gap: 10px; }
  .card-back .brand-name { font-size: 17px; letter-spacing: .3px; }
  .card-back .brand-dot { width: 16px; height: 16px; }
  .holder {
    padding-left: 26px;
    display: flex;
    flex-direction: column;
    gap: 4px;
  }
  .holder-name {
    font-size: 13px;
    font-weight: 600;
    color: var(--purple);
  }
  .holder-role {
    font-size: 9px;
    font-weight: 500;
    color: var(--orange);
    letter-spacing: 1.5px;
    text-transform: uppercase;
  }
  .divider {
    width: 1px;
    height: 170px;
    background: var(--rule);
    flex: none;
  }
  .contact-list {
    list-style: none;
    display: flex;
    flex-direction: column;
    gap: 16px;
    flex: 1;
  }
  .contact-item {
    display: flex;
    align-items: center;
    gap: 10px;
    font-size: 8.5px;
    line-height: 1.45;
    color: var(--ink);
  }
  .contact-icon {
    width: 22px; height: 22px;
    border-radius: 50%;
    background: var(--orange);
    flex: none;
    display: flex;
    align-items: center;
    justify-content: center;
  }
  .contact-icon svg { width: 12px; height: 12px; fill: none; stroke: #fff; stroke-width: 2; stroke-linecap: round; stroke-linejoin: round; }
</style>
</head>
<body>
  <section class="card card-front" aria-label="Card front">
    <div class="brand">
      <span class="brand-dot"></span>
      <span class="brand-name">Velora<br>Formulations</span>
    </div>
  </section>

  <section class="card card-back" aria-label="Card back">
    <div class="identity">
      <div class="brand">
        <span class="brand-dot"></span>
        <span class="brand-name">Velora<br>Formulations</span>
      </div>
      <div class="holder">
        <span class="holder-name">Your Name</span>
        <span class="holder-role">Designation</span>
      </div>
    </div>
    <span class="divider"></span>
    <ul class="contact-list">
      <li class="contact-item">
        <span class="contact-icon"><svg viewBox="0 0 24 24"><path d="M12 22s7-7 7-12a7 7 0 0 0-14 0c0 5 7 12 7 12z"/><circle cx="12" cy="10" r="2.5"/></svg></span>
        <span>14 Harbor Crest Lane, Suite 3B,<br>Eastfield Industrial Park, Westbrook<br>Ridgeview District, 40211</span>
      </li>
      <li class="contact-item">
        <span class="contact-icon"><svg viewBox="0 0 24 24"><rect x="3" y="6" width="18" height="12" rx="1"/><path d="M3 7l9 6 9-6"/></svg></span>
        <span>info@veloraformulations.com<br>velora.formulations@mail.com</span>
      </li>
      <li class="contact-item">
        <span class="contact-icon"><svg viewBox="0 0 24 24"><circle cx="12" cy="12" r="9"/><path d="M3 12h18M12 3c3 3 3 15 0 18M12 3c-3 3-3 15 0 18"/></svg></span>
        <span>www.veloraformulations.com</span>
      </li>
      <li class="contact-item">
        <span class="contact-icon"><svg viewBox="0 0 24 24"><path d="M5 4h4l2 5-2.5 1.5a11 11 0 0 0 5 5L15 13l5 2v4a1 1 0 0 1-1 1A16 16 0 0 1 4 5a1 1 0 0 1 1-1z"/></svg></span>
        <span>044-3970864</span>
      </li>
    </ul>
  </section>
</body>
</html>
```